Can you design the Future of Mealworm Pet Food Packaging for me?

Project Overview:
We are seeking a dynamic and visually striking product label design for our range of mealworm pet food supplements. The label must effectively showcase the product, accommodate various container and packaging sizes, and include essential information such as a barcode, ingredients list, company address, and instructions for use. The design should exude positivity, capture the attention of consumers, and convey the quality and value of the product.

Target Audience:
Our target audience consists of health-conscious pet owners, aged 25-55, who prioritize quality, sustainability, and aesthetic appeal in their purchasing decisions. They are drawn to visually appealing packaging that conveys trustworthiness and authenticity.

Key Objectives:

Create a visually impactful label design that stands out on shelves and online platforms.
Clearly showcase the product while leaving space for essential information.
Ensure versatility to fit various container and packaging sizes.
Convey positivity, quality, and authenticity to resonate with our target audience.
Facilitate ease of use and readability for consumers.

Design Requirements:

Product Showcase: The label should prominently feature the product, with high-quality imagery, words or illustrations that highlight its key attributes and appeal to the target audience.

Space for Essential Information:
The design must include designated areas for a barcode, ingredients list, company address, and instructions for use. These elements should be clearly legible and easily accessible to consumers.

Versatility: The label design should be adaptable to different container shapes and sizes, including bottles, jars, and pouches. It should maintain its visual impact and readability across various packaging formats.

Positive Visual Impact: Incorporate colors, fonts, and imagery that evoke feelings of positivity, vitality, and well-being. Avoid clutter and maintain a clean, modern aesthetic. An example from a competitor company is attached for information.

To help provide you some focus, the first labels to be used in our production will measure 14cm x 6cm and the contents will weigh 20g

Please contact me if you have any questions about this brief or would like more info to help with your design. Thank you and I look forward to seeing your design.

Target Market(s)

Target Audience: Our target audience consists of health-conscious pet owners, aged 25-55, who prioritize quality, sustainability, and aesthetic appeal in their purchasing decisions. They are drawn to visually appealing packaging that conveys trustworthiness and authenticity.

Industry/Entity Type

Pet Food

Requirements
Must have
• Key Objectives: Create a visually impactful label design that stands out on shelves and online platforms. Clearly showcase the product while leaving space for essential information. Ensure versatility to fit various container and packaging sizes. Convey positivity, quality, and authenticity to resonate with our target audience. Facilitate ease of use and readability for consumers.
Nice to have
• Maintain a clean, modern aesthetic
Should not have
• Avoid clutter

```html
<!DOCTYPE html>
<html lang="en">
<head>
<meta charset="utf-8">
<title>Brookline Goldfish with Mealworm – Label</title>
<link rel="stylesheet" href="https://fonts.googleapis.com/css2?family=Montserrat:wght@500;700&family=Questrial&family=Roboto+Condensed:wght@300&display=swap">
<style>
  :root {
    --page: #ffffff;
    --blue-deep: #2a7fc9;
    --blue-bright: #1f9ad8;
    --orange: #d5561e;
    --white: #ffffff;
    --ink: #1c1c1c;
    --silver-light: #f4f4f4;
    --silver-mid: #c9c9c9;
    --silver-dark: #8e8e8e;
    --fish-orange: #f07a1a;
    --fish-gold: #f6c23a;
  }
  html, body {
    margin: 0;
    width: 1200px;
    height: 1200px;
    overflow: hidden;
    background: var(--page);
  }
  .label {
    position: absolute;
    left: 40px;
    top: 94px;
    width: 1120px;
    height: 1012px;
    overflow: hidden;
    background: linear-gradient(90deg, var(--blue-deep) 0%, var(--blue-bright) 55%, var(--blue-deep) 100%);
  }
  .label__shapes {
    position: absolute;
    inset: 0;
  }
  .brand-name {
    position: absolute;
    top: 118px;
    left: 0;
    right: 0;
    text-align: center;
    font-family: "Questrial", sans-serif;
    font-size: 50px;
    letter-spacing: 2px;
    color: var(--white);
    margin: 0;
  }
  .product-name {
    position: absolute;
    top: 300px;
    left: 0;
    right: 0;
    text-align: center;
    margin: 0;
    padding-left: 40px;
    font-family: "Montserrat", sans-serif;
    font-weight: 700;
    font-size: 184px;
    line-height: 1;
    letter-spacing: -4px;
    color: var(--white);
  }
  .flavour-pill {
    position: absolute;
    left: 278px;
    top: 482px;
    width: 578px;
    height: 82px;
    border-radius: 40px 18px 40px 18px;
    background: linear-gradient(90deg, var(--silver-dark) 0%, var(--silver-light) 30%, var(--silver-mid) 60%, var(--silver-light) 85%, var(--silver-dark) 100%);
    display: flex;
    align-items: center;
    justify-content: center;
    font-family: "Montserrat", sans-serif;
    font-weight: 500;
    font-size: 42px;
    letter-spacing: 7px;
    color: var(--ink);
  }
  .tagline {
    position: absolute;
    top: 592px;
    left: 220px;
    width: 680px;
    margin: 0;
    text-align: center;
    font-family: "Questrial", sans-serif;
    font-size: 33px;
    line-height: 44px;
    color: var(--white);
  }
  .hero-fish {
    position: absolute;
    left: 0;
    top: 354px;
    width: 196px;
    height: 368px;
    border-radius: 0 120px 140px 0;
    background: linear-gradient(160deg, var(--fish-orange) 0%, #e9621a 45%, var(--fish-gold) 100%);
  }
  .benefits {
    position: absolute;
    top: 796px;
    left: 300px;
    display: flex;
    gap: 60px;
  }
  .benefit {
    display: flex;
    flex-direction: column;
    align-items: center;
    gap: 26px;
    font-family: "Roboto Condensed", sans-serif;
    font-weight: 300;
    font-size: 40px;
    color: var(--white);
    white-space: nowrap;
  }
  .benefit__icon {
    width: 66px;
    height: 62px;
    background: rgba(255, 255, 255, 0.85);
    border-radius: 6px;
  }
  .net-weight {
    position: absolute;
    left: 960px;
    top: 700px;
    width: 250px;
    height: 270px;
    border-radius: 50%;
    background: radial-gradient(circle at 60% 45%, var(--silver-light) 0%, var(--silver-mid) 55%, var(--silver-dark) 100%);
    font-family: "Questrial", sans-serif;
    font-size: 40px;
    line-height: 48px;
    color: var(--ink);
    text-align: center;
    box-sizing: border-box;
    padding: 70px 60px 0 0;
  }
</style>
</head>
<body>
  <section class="label" aria-label="Brookline Goldfish food label">
    <svg class="label__shapes" viewBox="0 0 1120 1012" width="1120" height="1012" aria-hidden="true">
      <path class="label__divider" d="M0 140 Q560 300 1120 140" fill="none" stroke="#ffffff" stroke-width="10"/>
      <path class="label__base" d="M0 772 Q300 720 560 703 Q860 690 1120 741 L1120 1012 L0 1012 Z" fill="#d5561e"/>
    </svg>

    <p class="brand-name">Brookline</p>

    <h1 class="product-name">Goldfish</h1>

    <div class="flavour-pill">WITH MEALWORM</div>

    <p class="tagline">Natural food, crammed with goodness for all coldwater fish, with no artificial colours</p>

    <div class="hero-fish" role="img" aria-label="Illustration of an orange goldfish swimming in from the left edge"></div>

    <ul class="benefits" style="list-style:none;margin:0;padding:0;">
      <li class="benefit">
        <span class="benefit__icon" role="img" aria-label="Icon of a person fishing from a boat"></span>
        Sustainably Harvested
      </li>
      <li class="benefit">
        <span class="benefit__icon" role="img" aria-label="Icon of sea kelp"></span>
        with Sea Kelp
      </li>
    </ul>

    <div class="net-weight">NT. Wt.<br>20g</div>
  </section>
</body>
</html>
```